Budget Brand Responsive Website

Flat vector style website needed for value based IT support company. looking for clean, illustration intensive based design. Current test site can be found at www.quen-vo.co.uk and holding page it www.quenvo.co.uk this will show text and services, please feel free to use placeholder text if you think we need alternative text in places. Emphasis should be on low cost support and services listed on the site, would be nice to see costs in bold images. important colors are the blue, orange and white, see holding page and attached image of an advert

It Company

```html
<!DOCTYPE html>
<html lang="en">
<head>
<meta charset="utf-8">
<title>Quenvo IT – Low Cost IT Support</title>
<link href="https://fonts.googleapis.com/css2?family=Roboto:wght@300;400;500;700;900&display=swap" rel="stylesheet">
<style>
:root{
  --blue:#1f4f95;
  --blue-dark:#173c75;
  --blue-light:#2d6cc0;
  --orange:#e8761f;
  --white:#ffffff;
  --grey-bg:#f1f2f4;
  --grey-line:#d9dde3;
  --text:#4a4f57;
  --text-light:#8a9099;
  --footer:#25282d;
  --footer-bottom:#1b1d21;
}
*{box-sizing:border-box;margin:0;padding:0}
html,body{width:1200px;height:3000px;overflow:hidden}
body{font-family:"Roboto",Arial,sans-serif;color:var(--text);background:var(--white)}
.page{width:1200px;height:3000px;position:relative}

/* header */
.site-header{height:70px;display:flex;align-items:center;justify-content:space-between;padding:0 100px;background:var(--white);border-bottom:1px solid var(--grey-line)}
.brand{display:flex;align-items:center;gap:10px;font-weight:900;font-size:28px;color:var(--blue);letter-spacing:1px}
.brand-mark{width:24px;height:24px;border-radius:50%;background:var(--orange)}
.main-nav{display:flex}
.main-nav a{font-size:13px;font-weight:500;color:var(--blue);text-decoration:none;padding:10px 18px;letter-spacing:.5px}
.main-nav a.active{background:var(--orange);color:var(--white)}

/* hero */
.hero{position:relative;height:640px}
.hero-art{position:absolute;inset:0;background:linear-gradient(180deg,#e9edf1 0%,#dfe5ea 60%,#cfd8e0 100%)}
.hero-title{position:absolute;left:0;right:0;top:300px;text-align:center;font-size:46px;font-weight:900;color:var(--white);letter-spacing:1px;text-shadow:0 2px 6px rgba(0,0,0,.25)}
.hero-dots{position:absolute;right:110px;bottom:24px;display:flex;gap:8px}
.hero-dots span{width:10px;height:10px;border-radius:50%;background:#9aa3ad}
.hero-dots span.on{background:var(--orange)}

/* tied down band */
.promo-band{height:190px;background:linear-gradient(180deg,var(--blue-light),var(--blue));color:var(--white);text-align:center;padding:22px 150px}
.promo-band h2{font-size:24px;font-weight:700;color:var(--orange);margin-bottom:12px}
.promo-band p{font-size:12px;line-height:1.6;opacity:.9;margin-bottom:16px}
.promo-band .call{font-size:24px;font-weight:700}
.promo-band .call b{color:var(--orange)}

/* section heading */
.section-title{text-align:center;font-size:30px;font-weight:700;color:var(--blue-dark);padding-top:34px}
.section-title::after{content:"";display:block;width:60px;height:3px;background:var(--orange);margin:12px auto 0}

/* services */
.services{height:320px;background:var(--white)}
.service-grid{display:flex;justify-content:center;gap:32px;margin-top:28px}
.service{width:130px;text-align:center}
.service-icon{width:80px;height:80px;border-radius:50%;border:3px solid var(--blue);margin:0 auto 12px;display:flex;align-items:center;justify-content:center}
.service h3{font-size:14px;font-weight:700;color:var(--blue-dark);margin-bottom:6px}
.service p{font-size:11px;line-height:1.5;color:var(--text-light)}

/* pricing */
.pricing{height:540px;background:var(--grey-bg)}
.price-grid{display:flex;justify-content:center;align-items:flex-end;margin-top:40px;gap:6px}
.plan{width:250px;background:var(--white);border:1px solid var(--grey-line);text-align:center}
.plan-head{background:#cfdcee;padding:14px 10px;color:var(--blue-dark)}
.plan-head h3{font-size:22px;font-weight:700}
.plan-head p{font-size:11px;margin-top:4px}
.plan.featured .plan-head{background:var(--orange);color:var(--white);padding:22px 10px}
.plan ul{list-style:none}
.plan li{font-size:12px;padding:14px 0;border-bottom:1px solid var(--grey-line)}
.plan li:nth-child(odd){background:#f8f9fb}
.btn{display:inline-block;font-size:12px;font-weight:700;color:var(--white);background:var(--blue);padding:10px 18px;margin:18px 0;letter-spacing:.5px}
.btn.orange{background:var(--orange)}

/* about */
.about{height:300px;text-align:center}
.about p{width:860px;margin:20px auto 0;font-size:13px;line-height:1.7;color:var(--text-light)}

/* feature panels */
.features{display:flex;justify-content:center;gap:30px;height:280px;padding-top:20px}
.feature{width:400px;height:250px;background:linear-gradient(160deg,var(--blue-light),var(--blue-dark));color:var(--white);padding:26px 30px;text-align:center}
.feature h3{font-size:22px;font-weight:700;margin-bottom:18px}
.feature p{font-size:12px;line-height:1.75;opacity:.9}

/* map & offices */
.locations{position:relative;height:240px;margin-top:60px}
.map{position:absolute;inset:0;background:linear-gradient(135deg,#dfe6dc,#e9ede4 50%,#d6dde6)}
.office-row{position:absolute;left:100px;right:100px;top:40px;display:flex;gap:10px}
.office{flex:1;background:var(--white);padding:14px 16px;box-shadow:0 2px 6px rgba(0,0,0,.15);font-size:12px;line-height:1.6}
.office h4{font-size:13px;color:var(--blue-dark);font-weight:700}

/* footer */
.site-footer{background:var(--footer);height:320px;color:#a6abb3;display:flex;gap:50px;padding:40px 100px}
.footer-col h4{color:var(--white);font-size:16px;font-weight:700;margin-bottom:14px}
.footer-col p,.footer-col li{font-size:12px;line-height:1.8;list-style:none}
.footer-brand{width:290px}
.footer-brand .brand{color:var(--white);margin-bottom:16px}
.footer-legal{width:170px}
.footer-news{width:260px}
.input{width:220px;height:32px;background:var(--white);margin:12px 0 10px;font-size:12px;color:#999;padding:8px}
.footer-social{width:160px}
.footer-social li{display:flex;align-items:center;gap:10px;margin-bottom:8px}
.dot{width:22px;height:22px;border-radius:50%;background:var(--blue-light)}
.footer-bottom{background:var(--footer-bottom);height:40px;text-align:center;font-size:11px;color:#7c818a;line-height:40px}
</style>
</head>
<body>
<div class="page">

<header class="site-header">
  <div class="brand"><span class="brand-mark"></span>QUENVO IT</div>
  <nav class="main-nav">
    <a class="active">HOME</a><a>SUPPORT</a><a>SERVICES</a><a>ABOUT</a><a>CONTACT</a>
  </nav>
</header>

<section class="hero">
  <div class="hero-art" role="img" aria-label="Flat illustration of a desk with laptop, phone, tablet, coffee cup and office items seen from above"></div>
  <h1 class="hero-title">WE MAKE IT SIMPLER AND FAIRER</h1>
  <div class="hero-dots"><span class="on"></span><span></span><span></span></div>
</section>

<section class="promo-band">
  <h2>DON'T GET TIED DOWN!</h2>
  <p>We don't believe any local business should pay for IT support you don't need. Our simple monthly plans let you pick only the services that suit you today, with no long contracts, no hidden charges and friendly engineers on hand. If you are unhappy, simply leave at any time with thirty days notice, because we are sure you will stay for good service.</p>
  <div class="call">Call us today on <b>01000 111 222</b></div>
</section>

<section class="services">
  <h2 class="section-title">SERVICES TAILORED FOR YOU</h2>
  <div class="service-grid">
    <div class="service">
      <div class="service-icon"><svg width="40" height="40" viewBox="0 0 40 40" fill="none" stroke="#1f4f95" stroke-width="3"><circle cx="20" cy="14" r="7"/><path d="M7 36c0-8 6-12 13-12s13 4 13 12"/></svg></div>
      <h3>SUPPORT</h3><p>Unlimited remote support, monitoring and help desk from £8.50 a month</p>
    </div>
    <div class="service">
      <div class="service-icon"><svg width="40" height="40" viewBox="0 0 40 40" fill="none" stroke="#1f4f95" stroke-width="3"><path d="M10 6l6 8-4 4c2 5 5 8 10 10l4-4 8 6-4 6C18 36 4 22 4 12z"/></svg></div>
      <h3>VOICE</h3><p>Hosted phone systems, lines and numbers with low monthly prices</p>
    </div>
    <div class="service">
      <div class="service-icon"><svg width="40" height="40" viewBox="0 0 40 40" fill="none" stroke="#1f4f95" stroke-width="3"><circle cx="20" cy="20" r="15"/><path d="M5 20h30M20 5c-6 8-6 22 0 30M20 5c6 8 6 22 0 30"/></svg></div>
      <h3>INTERNET</h3><p>Fast broadband and fibre lines for every size of office</p>
    </div>
    <div class="service">
      <div class="service-icon"><svg width="40" height="40" viewBox="0 0 40 40" fill="none" stroke="#1f4f95" stroke-width="3"><rect x="9" y="18" width="22" height="16"/><path d="M13 18v-6a7 7 0 0 1 14 0v6"/></svg></div>
      <h3>SECURITY</h3><p>Virus protection, firewalls and email filters to keep you safe</p>
    </div>
    <div class="service">
      <div class="service-icon"><svg width="40" height="40" viewBox="0 0 40 40" fill="none" stroke="#1f4f95" stroke-width="3"><rect x="7" y="6" width="26" height="12"/><rect x="7" y="22" width="26" height="12"/><circle cx="13" cy="12" r="1.5"/><circle cx="13" cy="28" r="1.5"/></svg></div>
      <h3>HOSTING</h3><p>Reliable web and email hosting from just £2.00 a month</p>
    </div>
    <div class="service">
      <div class="service-icon"><svg width="40" height="40" viewBox="0 0 40 40" fill="none" stroke="#1f4f95" stroke-width="3"><path d="M11 30a7 7 0 0 1 0-14 10 10 0 0 1 19 2 6 6 0 0 1 0 12z"/></svg></div>
      <h3>CLOUD</h3><p>Online backup, private servers and virtual desktops on demand</p>
    </div>
  </div>
</section>

<section class="pricing">
  <h2 class="section-title">PRICING FOR OUR MOST POPULAR SERVICES</h2>
  <div class="price-grid">
    <div class="plan featured">
      <div class="plan-head"><h3>SUPPORT</h3><p>Unlimited Remote Support</p></div>
      <ul><li>Workstations £8.50</li><li>Virus £3.00</li><li>Servers £45.00</li></ul>
      <span class="btn">MORE DETAILS</span>
    </div>
    <div class="plan">
      <div class="plan-head"><h3>VOICE</h3><p>Lower Rates and Call Charges</p></div>
      <ul><li>PBX from £49.00</li><li>Line rental from £11.00</li><li>Phone numbers from £3.00</li></ul>
      <span class="btn">MORE DETAILS</span>
    </div>
    <div class="plan">
      <div class="plan-head"><h3>HOSTING</h3><p>Flexible and Secure</p></div>
      <ul><li>Email hosting from £2.00</li><li>Email protection from £1.00</li><li>OfficeDesk from £3.75</li></ul>
      <span class="btn">MORE DETAILS</span>
    </div>
    <div class="plan">
      <div class="plan-head"><h3>CLOUD</h3><p>Reduce Costs and Increase Performance</p></div>
      <ul><li>Online Backup</li><li>Private Cloud Servers</li><li>Virtual Desktops</li></ul>
      <span class="btn">MORE DETAILS</span>
    </div>
  </div>
</section>

<section class="about">
  <h2 class="section-title">ABOUT QUENVO IT</h2>
  <p>Quenvo IT is a value based managed service provider with years of industry experience. We are committed to delivering dependable technology solutions at a fair price, giving small and medium businesses the same quality of service that large firms enjoy.</p>
  <p>We have a portfolio of support services and products offering a real choice for your business. Our team recommends only what you need, with clear pricing and flexible plans that grow with you.</p>
  <span class="btn orange">READ MORE</span>
</section>

<section class="features">
  <div class="feature">
    <h3>TECHNICAL SUPPORT</h3>
    <p>Our highly skilled and certified engineers are on hand to support your business and solve problems quickly. We monitor your systems around the clock, fix issues remotely and visit when needed, so you can focus on running your business while we look after the technology.</p>
  </div>
  <div class="feature">
    <h3>WE EXCEED EXPECTATIONS</h3>
    <p>Unlike traditional IT support companies we keep prices low and service high. Our customers rate us highly for response times and friendly advice, and we are proud that most of our new clients come to us through recommendations from happy businesses nearby.</p>
  </div>
</section>

<section class="locations">
  <div class="map" role="img" aria-label="Street map showing office locations"></div>
  <div class="office-row">
    <div class="office"><h4>Essex Office</h4>Northfield Park Way<br>info@quenvo.co.uk</div>
    <div class="office"><h4>Hertfordshire Office</h4>Chesterfield Road<br>info@quenvo.co.uk</div>
    <div class="office"><h4>Support</h4>support@quenvo.co.uk<br>t: 01000 111 222</div>
    <div class="office"><h4>Sales</h4>sales@quenvo.co.uk<br>t: 01000 111 223</div>
  </div>
</section>

<footer>
  <div class="site-footer">
    <div class="footer-col footer-brand">
      <div class="brand"><span class="brand-mark"></span>QUENVO IT</div>
      <p>Simple and affordable IT support for local businesses, with clear pricing and no long contracts.</p>
      <p>www.quenvo.co.uk</p>
    </div>
    <div class="footer-col footer-legal">
      <h4>LEGAL</h4>
      <ul><li>Terms of Service</li><li>Privacy Policy</li><li>Cookies</li><li>Regulation</li></ul>
    </div>
    <div class="footer-col footer-news">
      <h4>NEWSLETTER</h4>
      <p>Get our latest tips and offers sent straight to your inbox each month.</p>
      <div class="input">Enter your email</div>
      <span class="btn" style="margin:0">Subscribe</span>
    </div>
    <div class="footer-col footer-social">
      <h4>SOCIAL</h4>
      <ul><li><span class="dot"></span>Friendsy</li><li><span class="dot"></span>Chirpline</li><li><span class="dot"></span>RSS</li></ul>
    </div>
  </div>
  <div class="footer-bottom">© Copyright 2015 Quenvo IT. All rights reserved.</div>
</footer>

</div>
</body>
</html>
```